A Speech Therapy Business needs to update their logo

I need an update to the font and color of my logo to look more appealing. I am looking to open a private practice as a Speech Language Pathologist that caters to adults and children. It needs to be sophisticated and friendly at the same time. I want to keep the silhouette in my logo as is, just update the font and color for "Brightpath".
Industry/Entity Type
Business
Contact Information for Business Card
I want the business card to have my logo, my name (Odile Varn, CCC-SLP, TSSLD) and that I am a Bilingual Speech Language Pathologist. Also, include my phone number, (718) 555-0193. Include my website, Brightpathslp.example, and email address, odilevarn@brightpathslp.example
Look and feel

```html
<!DOCTYPE html>
<html lang="en">
<head>
<meta charset="utf-8">
<title>Brightpath – Business Card</title>
<link rel="stylesheet" href="https://fonts.googleapis.com/css2?family=Montserrat:wght@600;700&family=Lato:wght@400;700&display=swap">
<style>
  :root {
    --purple: #7b5ea7;
    --ink: #1c1c1c;
    --card-white: #f6f7f8;
    --backdrop: #e9e6e1;
    --band-text: #ffffff;
  }
  * { margin: 0; padding: 0; box-sizing: border-box; }
  html, body {
    width: 1200px; height: 1000px; overflow: hidden;
    background: var(--backdrop);
  }
  .stage { position: relative; width: 1200px; height: 1000px; }

  .card {
    position: absolute;
    box-shadow: 0 3px 8px rgba(0,0,0,0.18);
  }

  /* Front card sits on top of the back card */
  .card-front {
    left: 203px; top: 253px; width: 490px; height: 271px;
    background: var(--card-white);
    z-index: 2;
  }
  .front-logo {
    position: absolute; left: 46px; top: 78px; width: 222px; height: 92px;
    display: flex; align-items: center; justify-content: center;
  }
  .brand-name {
    font-family: "Montserrat", sans-serif; font-weight: 700;
    letter-spacing: 0.5px;
  }
  .front-logo .brand-name { font-size: 30px; color: var(--ink); }

  .identity { position: absolute; left: 287px; top: 80px; }
  .identity .person-name {
    font-family: "Montserrat", sans-serif; font-weight: 700;
    font-size: 25px; color: var(--purple); line-height: 1.1;
  }
  .identity .credentials {
    font-family: "Montserrat", sans-serif; font-weight: 600;
    font-size: 15px; color: var(--ink); margin-top: 3px;
  }
  .identity .role {
    font-family: "Lato", sans-serif; font-size: 12.5px; color: var(--ink);
    line-height: 1.3; margin-top: 5px; width: 170px;
  }

  .contact-band {
    position: absolute; left: 0; top: 214px; width: 100%; height: 41px;
    background: var(--purple);
    display: flex; align-items: center; justify-content: center;
    font-family: "Lato", sans-serif; font-size: 12px; color: var(--band-text);
    white-space: nowrap;
  }
  .contact-band .item { padding: 0 6px; }
  .contact-band .divider {
    width: 2px; height: 28px; background: var(--band-text); flex: none;
  }

  /* Back card */
  .card-back {
    left: 522px; top: 487px; width: 498px; height: 284px;
    background: var(--purple);
    display: flex; align-items: center; justify-content: center;
    z-index: 1;
  }
  .card-back .brand-name { font-size: 44px; color: #ffffff; }
</style>
</head>
<body>
<main class="stage">
  <section class="card card-front">
    <div class="front-logo">
      <span class="brand-name">Brightpath</span>
    </div>
    <div class="identity">
      <h1 class="person-name">Odile Varn</h1>
      <p class="credentials">CCC-SLP TSSLD</p>
      <p class="role">Bilingual Speech Language Pathologist</p>
    </div>
    <div class="contact-band">
      <span class="item">(718) 555-0193</span>
      <span class="divider"></span>
      <span class="item">www.brightpathslp.example</span>
      <span class="divider"></span>
      <span class="item">odilevarn@brightpathslp.example</span>
    </div>
  </section>

  <section class="card card-back">
    <span class="brand-name">Brightpath</span>
  </section>
</main>
</body>
</html>
```